Business Card Design

My business is writing crime novels to entertain readers. I write legal thrillers and mysteries. I need a card for publishers, agents, other authors, and media.

Industry/Entity Type

Legal

Contact Information for Business Card

Paul Ostrander
www.ostranderthrillers.example
paulbostrander@mailbox.example
0064 27 5139427

```html
<!DOCTYPE html>
<html lang="en">
<head>
<meta charset="utf-8">
<title>Paul Ostrander – Business Card</title>
<link href="https://fonts.googleapis.com/css2?family=Cabin:wght@700&family=Cabin+Condensed:wght@600&display=swap" rel="stylesheet">
<style>
  :root {
    --page-bg: #e8e5e0;
    --card-center: #3a3a3a;
    --card-edge: #1b1b1b;
    --accent-yellow: #f5e614;
    --name-grey: #c9c9c9;
    --frame-dark: #2a2a2a;
    --portrait-light: #9a9a9a;
    --portrait-dark: #4a4a4a;
  }
  * { box-sizing: border-box; margin: 0; padding: 0; }
  html, body {
    width: 1200px;
    height: 1181px;
    overflow: hidden;
    background: var(--page-bg);
  }
  .business-card {
    position: absolute;
    left: 194px;
    top: 355px;
    width: 816px;
    height: 470px;
    background: radial-gradient(ellipse at 55% 55%, var(--card-center) 0%, var(--card-edge) 75%);
    box-shadow: 0 8px 22px rgba(0,0,0,0.35);
    overflow: hidden;
  }
  .portrait-accent {
    position: absolute;
    left: 30px;
    top: 28px;
    width: 180px;
    height: 198px;
    background: var(--accent-yellow);
    transform: rotate(-8deg);
  }
  .portrait-frame {
    position: absolute;
    left: 44px;
    top: 41px;
    width: 156px;
    height: 177px;
    background: var(--frame-dark);
    padding: 6px;
    box-shadow: 0 3px 8px rgba(0,0,0,0.5);
  }
  .portrait-photo {
    width: 100%;
    height: 100%;
    background: linear-gradient(180deg, var(--portrait-light) 0%, #7d7d7d 55%, var(--portrait-dark) 100%);
  }
  .author-name {
    position: absolute;
    left: 180px;
    top: 215px;
    width: 480px;
    text-align: center;
    font-family: "Cabin Condensed", sans-serif;
    font-weight: 600;
    font-size: 62px;
    letter-spacing: 1px;
    color: var(--name-grey);
    text-transform: uppercase;
    line-height: 1;
    white-space: nowrap;
    transform: rotate(-12deg);
    transform-origin: center center;
  }
  .contact-row {
    position: absolute;
    left: 0;
    right: 0;
    top: 438px;
    display: flex;
    justify-content: center;
    gap: 16px;
    font-family: "Cabin", sans-serif;
    font-weight: 700;
    font-size: 15px;
    color: var(--accent-yellow);
  }
  .contact-item {
    display: flex;
    align-items: center;
    gap: 9px;
  }
  .contact-item::before {
    content: "";
    width: 7px;
    height: 7px;
    background: var(--accent-yellow);
    transform: rotate(45deg);
  }
</style>
</head>
<body>
  <div class="business-card">
    <div class="portrait-accent"></div>
    <div class="portrait-frame">
      <div class="portrait-photo" role="img" aria-label="Portrait photograph of the author"></div>
    </div>

    <div class="author-name">Paul Ostrander</div>

    <div class="contact-row">
      <span class="contact-item">0064 27 5139427</span>
      <span class="contact-item">paulbostrander@mailbox.example</span>
      <span class="contact-item">www.ostranderthrillers.example</span>
    </div>
  </div>
</body>
</html>
```